" Dar visibilidade para todo tipo de comercios do ramo de alimentação e informar suas promoções do dia. KiteBloom Experiências Gastronômicas incríveis ao seu redor, rápido fácil e barato, na palma da sua mão. O mundo todo come aqui! "

```html
<!DOCTYPE html>
<html lang="pt-BR">
<head>
<meta charset="UTF-8">
<title>KiteBloom – Papel timbrado</title>
<link href="https://fonts.googleapis.com/css2?family=Ubuntu:wght@400;700&display=swap" rel="stylesheet">
<style>
  :root {
    --backdrop: #bfc0c2;
    --paper: #ffffff;
    --orange: #f0922e;
    --maroon: #8b1a1a;
    --faint: #ececed;
    --footer-text: #f6e9e4;
  }
  * { margin: 0; padding: 0; box-sizing: border-box; }
  html, body {
    width: 1200px; height: 1200px; overflow: hidden;
    background: var(--backdrop);
    font-family: "Ubuntu", Arial, sans-serif;
  }
  .letterhead {
    position: absolute;
    left: 259px; top: 115px;
    width: 682px; height: 970px;
    background: var(--paper);
    box-shadow: 0 2px 6px rgba(0,0,0,0.15);
  }
  .brand {
    position: absolute;
    top: 34px; left: 0; right: 0;
    display: flex; justify-content: center; align-items: center; gap: 10px;
  }
  .brand-dot {
    width: 34px; height: 34px; border-radius: 50%;
    background: var(--orange);
  }
  .brand-name {
    font-weight: 700; font-size: 34px; color: var(--maroon);
    letter-spacing: 0.5px;
  }
  .brand-mark-faint {
    position: absolute;
    left: 141px; top: 320px;
    width: 400px; height: 400px; border-radius: 50%;
    background: var(--faint);
  }
  .accent-rule {
    position: absolute;
    left: 0; right: 0; top: 880px;
    height: 9px; background: var(--orange);
  }
  .footer-band {
    position: absolute;
    left: 0; right: 0; bottom: 0;
    height: 67px; background: var(--maroon);
    display: flex; flex-direction: column; justify-content: center; align-items: center; gap: 8px;
    color: var(--footer-text); font-size: 10px;
  }
  .contact-row { display: flex; gap: 22px; align-items: center; }
  .contact-item { display: flex; align-items: center; gap: 6px; }
  .contact-icon { width: 13px; height: 13px; flex: none; }
</style>
</head>
<body>
  <main class="letterhead">
    <header class="brand">
      <span class="brand-dot"></span>
      <span class="brand-name">KiteBloom</span>
    </header>

    <div class="brand-mark-faint" aria-hidden="true"></div>

    <div class="accent-rule"></div>

    <footer class="footer-band">
      <div class="contact-row">
        <span class="contact-item">
          <svg class="contact-icon" viewBox="0 0 14 14"><circle cx="7" cy="7" r="7" fill="#f0922e"/><path d="M4.5 3.8l1.3-.3.8 1.8-.8.6c.4.9 1 1.5 1.9 1.9l.6-.8 1.8.8-.3 1.3c-3 0-5.3-2.3-5.3-5.3z" fill="#fff"/></svg>
          +55 11 4000-1234
        </span>
        <span class="contact-item">
          <svg class="contact-icon" viewBox="0 0 14 14"><circle cx="7" cy="7" r="7" fill="#f0922e"/><rect x="3.5" y="4.5" width="7" height="5" fill="none" stroke="#fff" stroke-width="1"/><path d="M3.5 4.5l3.5 3 3.5-3" fill="none" stroke="#fff" stroke-width="1"/></svg>
          ola@kitebloom.com.br
        </span>
        <span class="contact-item">
          <svg class="contact-icon" viewBox="0 0 14 14"><circle cx="7" cy="7" r="7" fill="#f0922e"/><circle cx="7" cy="7" r="3.5" fill="none" stroke="#fff" stroke-width="1"/><path d="M3.5 7h7M7 3.5c-1.5 2-1.5 5 0 7M7 3.5c1.5 2 1.5 5 0 7" fill="none" stroke="#fff" stroke-width="0.8"/></svg>
          www.kitebloom.com.br
        </span>
      </div>
      <div class="contact-row">
        <span class="contact-item">
          <svg class="contact-icon" viewBox="0 0 14 14"><circle cx="7" cy="7" r="7" fill="#f0922e"/><path d="M7 11s-3-3.2-3-5.2a3 3 0 016 0C10 7.8 7 11 7 11z" fill="#fff"/><circle cx="7" cy="5.8" r="1" fill="#f0922e"/></svg>
          Rua das Flores, 120 - Centro - São Paulo - SP
        </span>
      </div>
    </footer>
  </main>
</body>
</html>
```